Modern Business Card Design for Independent Urban Music Label

We need a card design for an independent urban music label called Copper Kite Records based in London. We develop and promote urban British music artists. We attend lots of high profile events with high profile industry people and want a card that comes across both on-brand and sophisticated, professional, trustworthy. I have attached our logo - please use the black and orange version in the upper left HOWEVER we are open to seeing other colors than the orange used though we want the shape of the logo to remain the same.

Info to please include:
Name
Position
Phone
Email
Website

Additional Info:
Twitter: @CopperKiteRecsUK
Insta: @CopperKiteRecs

Target Market(s)

Industry professionals and others artists

Industry/Entity Type

Business

Contact Information for Business Card

Info to please include:
Name
Position
Phone
Email
Website

Additional Info:
Twitter: @CopperKiteRecsUK
Insta: @CopperKiteRecs

Requirements
Must have
• Logo, company name
• Info to please include:
• Name
• Position
• Phone
• Email
• Website
Nice to have
• Twitter: @CopperKiteRecsUK
• Insta: @CopperKiteRecs
• If it can be done so that it doesn't look cluttered

```html
<!DOCTYPE html>
<html lang="en">
<head>
<meta charset="utf-8">
<title>Copper Kite Records – Business Card</title>
<link href="https://fonts.googleapis.com/css2?family=Lato:wght@400;700;900&display=swap" rel="stylesheet">
<style>
  :root {
    --backdrop: #222224;
    --copper-light: #f6b877;
    --copper: #e39552;
    --copper-deep: #d27c3a;
    --ink: #2a2526;
    --paper: #f4f4f4;
    --white: #ffffff;
  }
  * { margin: 0; padding: 0; box-sizing: border-box; }
  html, body {
    width: 1200px; height: 900px; overflow: hidden;
    background: var(--backdrop);
    font-family: "Lato", sans-serif;
  }
  .canvas { position: relative; width: 1200px; height: 900px; }

  .card {
    position: absolute; width: 560px; height: 320px;
    border-radius: 4px; overflow: hidden;
    box-shadow: 0 18px 40px rgba(0,0,0,.55);
  }

  /* Front */
  .card-front {
    left: 90px; top: 70px;
    background: radial-gradient(ellipse at 70% 30%, var(--copper-light), var(--copper) 55%, var(--copper-deep));
  }
  .card-front .swoosh { position: absolute; inset: 0; }
  .brand-front {
    position: absolute; left: 0; right: 0; top: 118px;
    display: flex; align-items: center; justify-content: center; gap: 10px;
    color: var(--white); font-weight: 900; font-size: 20px; letter-spacing: 2px;
    text-transform: uppercase;
  }
  .brand-dot { width: 14px; height: 14px; border-radius: 50%; background: var(--white); }
  .front-web {
    position: absolute; left: 270px; top: 256px;
    color: var(--white); font-size: 16px; letter-spacing: .5px;
  }

  /* Back */
  .card-back { left: 550px; top: 500px; background: var(--ink); }
  .card-back .layout { position: absolute; inset: 0; }
  .brand-back {
    position: absolute; left: 0; width: 280px; top: 115px;
    display: flex; align-items: center; justify-content: center; gap: 8px;
    color: var(--copper); font-weight: 900; font-size: 15px; letter-spacing: 1.5px;
    text-transform: uppercase;
  }
  .brand-back .brand-dot { width: 11px; height: 11px; background: var(--copper); }
  .holder { position: absolute; left: 320px; top: 96px; }
  .holder-name { color: var(--copper); font-weight: 900; font-size: 17px; }
  .holder-role { color: var(--ink); font-size: 13px; margin-top: 1px; }

  .contact-list {
    position: absolute; left: 296px; top: 190px; list-style: none;
    color: var(--white); font-size: 15px;
  }
  .contact-list li { display: flex; align-items: center; gap: 9px; height: 22px; }
  .contact-icon {
    width: 15px; height: 15px; border-radius: 2px; background: var(--copper);
    display: flex; align-items: center; justify-content: center; flex: none;
  }
  .contact-icon svg { width: 11px; height: 11px; }
</style>
</head>
<body>
<main class="canvas">

  <section class="card card-front" aria-label="Business card front">
    <svg class="swoosh" viewBox="0 0 560 320" preserveAspectRatio="none" aria-hidden="true">
      <path d="M0 300 Q 260 190 560 205 L560 320 L0 320 Z" fill="var(--ink)"/>
    </svg>
    <div class="brand-front"><span class="brand-dot"></span>Copper Kite Records</div>
    <p class="front-web">www.ckrecords.co.uk</p>
  </section>

  <section class="card card-back" aria-label="Business card back">
    <svg class="layout" viewBox="0 0 560 320" aria-hidden="true">
      <rect x="0" y="0" width="280" height="255" fill="var(--paper)"/>
      <polygon points="305,18 472,18 472,182 305,128" fill="var(--paper)"/>
      <rect x="496" y="28" width="40" height="272" fill="var(--paper)"/>
    </svg>
    <div class="brand-back"><span class="brand-dot"></span>Copper Kite Records</div>
    <div class="holder">
      <p class="holder-name">Maya Ellison</p>
      <p class="holder-role">Director</p>
    </div>
    <ul class="contact-list">
      <li><span class="contact-icon"><svg viewBox="0 0 10 10"><path d="M2 1 L4 1 L4.5 3 L3.3 3.8 Q4 5.8 6.2 6.7 L7 5.5 L9 6 L9 8 Q5 9.5 1 4 Z" fill="var(--ink)"/></svg></span>020 7946 0183</li>
      <li><span class="contact-icon"><svg viewBox="0 0 10 10"><rect x="1" y="2.5" width="8" height="5.5" fill="none" stroke="var(--ink)" stroke-width="1"/><path d="M1 2.5 L5 5.5 L9 2.5" fill="none" stroke="var(--ink)" stroke-width="1"/></svg></span>maya@ckrecords.co.uk</li>
      <li><span class="contact-icon"><svg viewBox="0 0 10 10"><circle cx="5" cy="5" r="3.8" fill="none" stroke="var(--ink)" stroke-width="1"/><ellipse cx="5" cy="5" rx="1.6" ry="3.8" fill="none" stroke="var(--ink)" stroke-width=".8"/><path d="M1.2 5 H8.8" stroke="var(--ink)" stroke-width=".8"/></svg></span>www.ckrecords.co.uk</li>
      <li><span class="contact-icon"></span>@CopperKiteRecsUK</li>
      <li><span class="contact-icon"></span>@CopperKiteRecs</li>
    </ul>
  </section>

</main>
</body>
</html>
```